" Nossa empresa fica aberta ao publico de seg a sexta das 8h as 21h Oferecemos varias opçoes de lanches(assados integrais,kibe de quinoa,coxinha fit,acai,saladas e sanduiches) e sucos naturais.alem do nosso produto chave,que sao as marmitas saudaveis,nas versoes frescas e congeladas,que podem ser consumidas no local ou em casa, ja que as embalagens sao proprias para microondas e congelador. Opçoes sem gluten,lactose e vegetarianas estao sempre no menu. A proposta é trazer o sabor e a simplicidade da comida caseira,de forma consciente e nutritiva. "

```html
<!DOCTYPE html>
<html lang="pt-BR">
<head>
<meta charset="UTF-8">
<title>Verdelia – cartão de visita</title>
<link rel="stylesheet" href="https://fonts.googleapis.com/css2?family=Nunito:wght@300;400;800&display=swap">
<style>
  :root {
    --bg: #e9ebe6;
    --paper: #ffffff;
    --green: #8cc63f;
    --green-light: #b5dc72;
    --ink: #2f3b24;
    --text: #5a5f55;
  }
  * { box-sizing: border-box; margin: 0; padding: 0; }
  html, body { width: 1200px; height: 1200px; overflow: hidden; }
  body {
    background: var(--bg);
    font-family: "Nunito", sans-serif;
    position: relative;
  }
  .card {
    position: absolute;
    left: 165px;
    width: 870px;
    height: 490px;
    background: var(--paper);
    box-shadow: 0 10px 30px rgba(40, 50, 30, 0.18);
    overflow: hidden;
  }
  .card--front { top: 80px; }
  .card--back { top: 630px; border-bottom: 12px solid var(--green); }

  .front-art { position: absolute; inset: 0; }
  .brand {
    position: absolute;
    display: flex;
    align-items: center;
    white-space: nowrap;
  }
  .brand__dot {
    border-radius: 50%;
    background: var(--green);
    flex: none;
  }
  .brand__name {
    font-weight: 800;
    color: var(--ink);
    letter-spacing: -1px;
    line-height: 1;
  }
  .card--front .brand {
    left: 50%; top: 50%;
    transform: translate(-50%, -50%);
    gap: 18px;
  }
  .card--front .brand__dot { width: 50px; height: 50px; }
  .card--front .brand__name { font-size: 64px; }

  .back-stripe {
    position: absolute;
    left: 0; top: 0; bottom: 0;
    width: 26px;
    background: var(--green);
  }
  .contact-list {
    position: absolute;
    left: 78px; top: 70px;
    list-style: none;
    display: flex;
    flex-direction: column;
    gap: 34px;
  }
  .contact-list li {
    display: flex;
    align-items: center;
    gap: 20px;
    font-weight: 300;
    font-size: 25px;
    color: var(--text);
    white-space: nowrap;
  }
  .contact-icon { width: 30px; height: 30px; flex: none; fill: var(--green); }
  .card--back .brand {
    right: 56px; top: 50%;
    transform: translateY(-50%);
    gap: 14px;
  }
  .card--back .brand__dot { width: 38px; height: 38px; }
  .card--back .brand__name { font-size: 44px; }
</style>
</head>
<body>

<section class="card card--front">
  <svg class="front-art" viewBox="0 0 870 490" role="img" aria-label="Painéis verdes com padrão suave de folhas">
    <defs>
      <linearGradient id="leafTone" x1="0" y1="0" x2="1" y2="1">
        <stop offset="0" stop-color="#b5dc72"/>
        <stop offset="1" stop-color="#8cc63f"/>
      </linearGradient>
    </defs>
    <polygon points="0,70 270,0 190,490 0,490" fill="url(#leafTone)"/>
    <polygon points="600,0 870,0 870,490 720,490" fill="url(#leafTone)"/>
  </svg>
  <div class="brand">
    <span class="brand__dot"></span>
    <span class="brand__name">Verdelia</span>
  </div>
</section>

<section class="card card--back">
  <div class="back-stripe"></div>
  <ul class="contact-list">
    <li>
      <svg class="contact-icon" viewBox="0 0 24 24"><path d="M6.6 10.8a15.5 15.5 0 0 0 6.6 6.6l2.2-2.2c.3-.3.7-.4 1-.2 1.1.4 2.3.6 3.6.6.6 0 1 .4 1 1V20c0 .6-.4 1-1 1A17 17 0 0 1 3 4c0-.6.4-1 1-1h3.5c.6 0 1 .4 1 1 0 1.3.2 2.5.6 3.6.1.3 0 .7-.2 1z"/></svg>
      <span>(xx)5210.4387 | (xx) 9734.2615</span>
    </li>
    <li>
      <svg class="contact-icon" viewBox="0 0 24 24"><path d="M2 5h20v14H2z" fill="none" stroke="#8cc63f" stroke-width="2"/><path d="M2 5l10 8 10-8" fill="none" stroke="#8cc63f" stroke-width="2"/></svg>
      <span>contato@verdelia.com.br</span>
    </li>
    <li>
      <svg class="contact-icon" viewBox="0 0 24 24"><rect x="3" y="3" width="18" height="18" rx="3"/></svg>
      <span>@verdelia.alimentos</span>
    </li>
    <li>
      <svg class="contact-icon" viewBox="0 0 24 24"><path d="M12 2a7 7 0 0 0-7 7c0 5 7 13 7 13s7-8 7-13a7 7 0 0 0-7-7zm0 9.5A2.5 2.5 0 1 1 12 6.5a2.5 2.5 0 0 1 0 5z"/></svg>
      <span>Rua das Palmeiras, 45 - Centro</span>
    </li>
  </ul>
  <div class="brand">
    <span class="brand__dot"></span>
    <span class="brand__name">Verdelia</span>
  </div>
</section>

</body>
</html>
```